Computer Training in the Education sector - Letterhead

We need a new letter head to be designed for the company. We provide computer training fro the Education Sector, both primary and private tertiary providers. The colours will need to tie in with the website www.lanternpathlearning.co.nz.
The company name is Lantern Path Co with the tag line of Computer Training for Educators.
The footer will need to have the following detail...
0508 KEY MENTOR
027 813 459
www.lanternpathlearning.co.nz / lessons@lanternpathlearning.co.nz
Updates

Thanks for the designs so far.

Some have watermarks in the background. Please don't worry about using watermarks as I will not be using a watermark in in a final design.
Regards,
Morris

Thank you for all the designs and the effort. There was some great concepts that came through.

Cheers
Morris

Industry/Entity Type

Computer

```html
<!DOCTYPE html>
<html lang="en">
<head>
<meta charset="utf-8">
<title>Lantern Path Co — Letterhead</title>
<link rel="stylesheet" href="https://fonts.googleapis.com/css2?family=Tinos:wght@400&display=swap">
<style>
  :root {
    --paper-light: #ffffff;
    --paper-tint: #e6fbfe;
    --paper-cyan: #a9f1fa;
    --ink-blue: #2b6fd6;
    --accent-blue: #2f7fe0;
    --accent-green: #8fe52b;
    --accent-orange: #f08a30;
  }
  * { margin: 0; padding: 0; box-sizing: border-box; }
  html, body {
    width: 848px;
    height: 1200px;
    overflow: hidden;
  }
  .letterhead {
    position: relative;
    width: 848px;
    height: 1200px;
    overflow: hidden;
    font-family: "Tinos", "Times New Roman", serif;
    color: var(--ink-blue);
    background:
      radial-gradient(ellipse 140% 110% at 95% 0%,
        var(--paper-light) 0%,
        var(--paper-light) 18%,
        var(--paper-tint) 50%,
        var(--paper-cyan) 100%);
  }
  .brand {
    position: absolute;
    top: 84px;
    right: 48px;
    display: flex;
    align-items: center;
    gap: 10px;
  }
  .brand-mark {
    width: 14px;
    height: 14px;
    border-radius: 50%;
    background: var(--ink-blue);
  }
  .brand-name {
    font-size: 26px;
    white-space: nowrap;
  }
  .web-address {
    position: absolute;
    top: 189px;
    right: 48px;
    font-size: 13px;
    letter-spacing: 1px;
    white-space: nowrap;
  }
  .contact {
    position: absolute;
    left: 572px;
    top: 1090px;
    list-style: none;
    font-size: 14.5px;
    letter-spacing: 1px;
    line-height: 25.5px;
    white-space: nowrap;
  }
  .accent-bars {
    position: absolute;
    left: 0;
    bottom: 56px;
    display: flex;
    flex-direction: column;
    gap: 10px;
  }
  .accent-bar {
    display: block;
    height: 14px;
    border-radius: 0 7px 7px 0;
  }
  .accent-bar.orange { width: 300px; background: var(--accent-orange); }
  .accent-bar.green { width: 230px; background: var(--accent-green); }
  .accent-bar.blue { width: 160px; background: var(--accent-blue); }
</style>
</head>
<body>
  <main class="letterhead">
    <header>
      <div class="brand">
        <span class="brand-mark"></span>
        <span class="brand-name">Lantern Path Co</span>
      </div>
      <p class="web-address">www.lanternpathlearning.co.nz</p>
    </header>

    <div class="accent-bars" aria-hidden="true">
      <span class="accent-bar orange"></span>
      <span class="accent-bar green"></span>
      <span class="accent-bar blue"></span>
    </div>

    <footer>
      <ul class="contact">
        <li>0508 KEY MENTOR</li>
        <li>027 813 459</li>
        <li>lessons@lanternpathlearning.co.nz</li>
      </ul>
    </footer>
  </main>
</body>
</html>
```